New Zealand Marlborough Sauvignon Blanc wine packaging design

We need packaging design for our new wine brand, Dunmore Hale. The wine is a New Zealand Marlborough Sauvignon Blanc. We would like the packaging will portray elegance and style with an understated label. We are looking for a label that portrays the elegance of the French Riviera. The label should be round or pill shaped.
Updates

Industry/Entity Type

Wine

Font styles to use
Serif
Sans Serif

Requirements
Must have
• The words in order of importance: Dunmore Hale, Sauvignon Blanc, Marlborough, New Zealand. It should be fit to the bottle posted in the links
Nice to have
• a pill shape or circular shape
Should not have
• Illustrations of wine bottles, wine glasses, or grapes

```html
<!DOCTYPE html>
<html lang="en">
<head>
<meta charset="utf-8">
<title>Dunmore Hale – Sauvignon Blanc label</title>
<link href="https://fonts.googleapis.com/css2?family=Marcellus&family=Pinyon+Script&family=Questrial&display=swap" rel="stylesheet">
<style>
  :root {
    --ink: #2b2626;
    --label-dark: #242323;
    --paper: #ffffff;
    --photo-cream: #f6ead3;
    --photo-amber: #b98a5e;
    --photo-umber: #5a4630;
    --photo-olive: #4a4a2c;
  }
  * { margin: 0; padding: 0; box-sizing: border-box; }
  html, body { width: 800px; height: 1200px; overflow: hidden; background: var(--paper); }
  .board { position: relative; width: 800px; height: 1200px; }

  .brand-mark {
    position: absolute; left: 30px; top: 60px; width: 200px; height: 140px;
    display: flex; flex-direction: column; align-items: center; justify-content: center; gap: 10px;
    color: var(--ink);
  }
  .brand-dot { width: 10px; height: 10px; border-radius: 50%; background: var(--ink); }
  .brand-name {
    font-family: "Marcellus", serif; font-size: 19px; letter-spacing: 5px; text-transform: uppercase;
    text-align: center; line-height: 1.5;
  }

  .label { position: absolute; }
  .label svg.frame { position: absolute; inset: 0; }
  .label-content {
    position: absolute; inset: 0; display: flex; flex-direction: column; align-items: center;
  }
  .label--dark { left: 268px; top: 72px; width: 210px; height: 362px; color: var(--paper); }
  .label--light-panel { position: absolute; left: 526px; top: 45px; width: 254px; height: 418px; background: var(--label-dark); }
  .label--light { left: 549px; top: 72px; width: 210px; height: 362px; color: var(--ink); }

  .label .label-brand {
    margin-top: 68px; font-family: "Marcellus", serif; font-size: 16px; letter-spacing: 4px;
    text-transform: uppercase; text-align: center; line-height: 1.6;
  }
  .label .label-dot { width: 8px; height: 8px; border-radius: 50%; background: currentColor; margin-top: 10px; }
  .varietal {
    margin-top: 58px; font-family: "Pinyon Script", cursive; font-size: 38px; line-height: 46px; text-align: center;
  }
  .region {
    margin-top: 12px; font-family: "Marcellus", serif; font-size: 15px; letter-spacing: 2px;
  }
  .country { margin-top: 6px; font-family: "Questrial", sans-serif; font-size: 9px; letter-spacing: 0.3px; }

  .product-photo {
    position: absolute; left: 0; top: 510px; width: 800px; height: 690px;
    background: linear-gradient(180deg, var(--photo-cream) 0%, #efd9b6 30%, var(--photo-amber) 52%, var(--photo-umber) 72%, var(--photo-olive) 100%);
  }
</style>
</head>
<body>
<main class="board">
  <div class="brand-mark">
    <span class="brand-dot"></span>
    <span class="brand-name">Dunmore<br>Hale</span>
  </div>

  <section class="label label--dark">
    <svg class="frame" width="210" height="362" viewBox="0 0 210 362">
      <rect x="1" y="1" width="208" height="360" rx="104" fill="none" stroke="var(--label-dark)" stroke-width="1.2"/>
      <rect x="6" y="6" width="198" height="350" rx="99" fill="var(--label-dark)"/>
    </svg>
    <div class="label-content">
      <div class="label-brand">Dunmore<br>Hale</div>
      <span class="label-dot"></span>
      <div class="varietal">Sauvignon<br>Blanc</div>
      <div class="region">MARLBOROUGH</div>
      <div class="country">New Zealand</div>
    </div>
  </section>

  <div class="label--light-panel"></div>
  <section class="label label--light">
    <svg class="frame" width="210" height="362" viewBox="0 0 210 362">
      <rect x="1" y="1" width="208" height="360" rx="104" fill="none" stroke="var(--paper)" stroke-width="1.2"/>
      <rect x="6" y="6" width="198" height="350" rx="99" fill="var(--paper)"/>
    </svg>
    <div class="label-content">
      <div class="label-brand">Dunmore<br>Hale</div>
      <span class="label-dot"></span>
      <div class="varietal">Sauvignon<br>Blanc</div>
      <div class="region">MARLBOROUGH</div>
      <div class="country">New Zealand</div>
    </div>
  </section>

  <div class="product-photo" role="img" aria-label="Photograph of the labelled wine bottle on a barrel top with cheese, olives and a glass of wine against a sunset vineyard"></div>
</main>
</body>
</html>
```